Banner Ad for our online service

We would like a banner ad for our online service that provides video reviews for people seeking apartments--flatscout.org. We would like you to include our attached logo in the banner and would also like visuals representing our service. The banner should be 300x250 pixels and should include the following text:

-Moving to Boston?
-We review apartments so you don't have to.
-Order now and receive $40 gift card.

We're open to all ideas. Thanks.

```html
<!DOCTYPE html>
<html lang="en">
<head>
<meta charset="utf-8">
<title>FlatScout Banner Ads</title>
<link href="https://fonts.googleapis.com/css2?family=Open+Sans:wght@400;600;700;800&display=swap" rel="stylesheet">
<style>
  :root {
    --stage: #3b1d10;
    --panel-dark: #262626;
    --panel-mid: #3a3a3a;
    --orange: #ec6c0c;
    --orange-text: #f07f1a;
    --white: #ffffff;
    --ink: #1d1d1d;
    --button-top: #ffd23a;
    --button-bottom: #f5a200;
    --footer: #ffffff;
  }
  * { box-sizing: border-box; margin: 0; padding: 0; }
  html, body {
    width: 1200px; height: 616px; overflow: hidden;
    background: var(--stage);
    font-family: "Open Sans", Arial, sans-serif;
  }
  .stage { position: relative; width: 1200px; height: 616px; }
  .banner-slot {
    position: absolute; top: 97px;
    width: 300px; height: 250px;
    transform: scale(1.446); transform-origin: 0 0;
  }
  .banner-slot.first { left: 127px; }
  .banner-slot.second { left: 584px; }
  .banner {
    position: relative; width: 300px; height: 250px; overflow: hidden;
    background: var(--footer);
    border: 1px solid #111;
  }
  .hero {
    position: absolute; left: 0; top: 0; width: 300px; height: 177px;
    background: linear-gradient(180deg, var(--panel-mid), var(--panel-dark));
  }
  .hero-photo {
    position: absolute; left: 0; top: 0; width: 300px; height: 177px;
    clip-path: polygon(206px 0, 300px 0, 300px 177px, 116px 177px);
  }
  .hero-photo.living {
    background: linear-gradient(160deg, #f2f1ee 0%, #d9d6cf 35%, #a73a22 62%, #5a1a10 80%, #3a2016 100%);
  }
  .hero-photo.kitchen {
    background: linear-gradient(160deg, #b9b6ae 0%, #e9e7e2 35%, #cfc8b8 60%, #9c9486 80%, #5e5a55 100%);
  }
  .play {
    position: absolute; left: 213px; top: 85px; width: 34px; height: 34px;
  }
  .headline {
    position: absolute; left: 17px; top: 13px;
    text-transform: uppercase; line-height: 1;
  }
  .headline .city-lead { color: var(--orange-text); font-size: 24px; font-weight: 600; letter-spacing: -0.3px; }
  .headline .city { color: var(--white); font-size: 27px; font-weight: 800; margin-top: 1px; letter-spacing: -0.3px; }
  .pitch {
    position: absolute; left: 17px; top: 82px;
    color: var(--white); font-size: 17px; font-weight: 400; line-height: 19px;
    text-transform: uppercase; letter-spacing: -0.5px;
  }
  .pitch .accent { color: var(--orange-text); font-weight: 600; }
  .offer-band {
    position: absolute; left: 0; top: 177px; width: 300px; height: 22px;
    background: var(--orange);
    color: var(--ink); font-size: 12.3px; font-weight: 600;
    line-height: 22px; text-align: center; text-transform: uppercase;
    letter-spacing: -0.2px;
  }
  .offer-band strong { font-weight: 800; }
  .footer {
    position: absolute; left: 0; top: 199px; width: 300px; height: 51px;
    background: linear-gradient(180deg, #ffffff 70%, #ececec);
  }
  .brand {
    position: absolute; left: 16px; top: 14px;
    display: flex; align-items: center; gap: 5px;
  }
  .brand-dot { width: 22px; height: 22px; border-radius: 50%; background: var(--orange); }
  .brand-name { color: var(--ink); font-size: 16px; font-weight: 600; letter-spacing: -0.5px; }
  .order-button {
    position: absolute; left: 164px; top: 10px; width: 121px; height: 27px;
    border-radius: 3px;
    background: linear-gradient(180deg, var(--button-top), var(--button-bottom));
    border: 1px solid #d98a00;
    display: flex; align-items: center; justify-content: center; gap: 6px;
    color: var(--ink); font-size: 14px; font-weight: 800; text-transform: uppercase;
  }
</style>
</head>
<body>
<div class="stage">

  <div class="banner-slot first">
    <div class="banner">
      <div class="hero">
        <div class="hero-photo living" role="img" aria-label="Bright modern living room with red sofa and dark coffee table"></div>
        <svg class="play" viewBox="0 0 34 34" aria-hidden="true">
          <circle cx="17" cy="17" r="16" fill="#2a2a2a" fill-opacity="0.85" stroke="#ffffff" stroke-opacity="0.5"/>
          <path d="M13 10 L25 17 L13 24 Z" fill="#ffffff"/>
        </svg>
        <div class="headline">
          <div class="city-lead">Moving to</div>
          <div class="city">Boston?</div>
        </div>
        <div class="pitch">
          We review<br><span class="accent">apartments</span><br>so you don’t<br>have to
        </div>
      </div>
      <div class="offer-band">Order now and receive <strong>$40 gift card</strong></div>
      <div class="footer">
        <div class="brand"><span class="brand-dot"></span><span class="brand-name">FlatScout</span></div>
        <div class="order-button">Order now
          <svg width="13" height="13" viewBox="0 0 13 13" aria-hidden="true"><circle cx="6.5" cy="6.5" r="6.5" fill="#1d1d1d"/><path d="M5 3.5 L8.5 6.5 L5 9.5 Z" fill="#ffc21a"/></svg>
        </div>
      </div>
    </div>
  </div>

  <div class="banner-slot second">
    <div class="banner">
      <div class="hero">
        <div class="hero-photo kitchen" role="img" aria-label="Clean white kitchen with tiled counter and stove"></div>
        <svg class="play" viewBox="0 0 34 34" aria-hidden="true">
          <circle cx="17" cy="17" r="16" fill="#2a2a2a" fill-opacity="0.85" stroke="#ffffff" stroke-opacity="0.5"/>
          <path d="M13 10 L25 17 L13 24 Z" fill="#ffffff"/>
        </svg>
        <div class="headline">
          <div class="city-lead">Moving to</div>
          <div class="city">Boston?</div>
        </div>
        <div class="pitch">
          We review<br><span class="accent">apartments</span><br>so you don’t<br>have to
        </div>
      </div>
      <div class="offer-band">Order now and receive <strong>$40 gift card</strong></div>
      <div class="footer">
        <div class="brand"><span class="brand-dot"></span><span class="brand-name">FlatScout</span></div>
        <div class="order-button">Order now
          <svg width="13" height="13" viewBox="0 0 13 13" aria-hidden="true"><circle cx="6.5" cy="6.5" r="6.5" fill="#1d1d1d"/><path d="M5 3.5 L8.5 6.5 L5 9.5 Z" fill="#ffc21a"/></svg>
        </div>
      </div>
    </div>
  </div>

</div>
</body>
</html>
```